2 x Digitize Logo | 2 x Business Cards | 2 x Fridge Magnets

We require 6 deliverables:
1. Residential logo redrawn (same just high quality for large print format).
2. Corporate logo redrawn (minor changes to wording and high quality for large print format).
3. New business card design for Furniture Removals (residential)
4. New business card design for Corporate Relocations (business)
5. New Fridge magnet for Furniture removals (residential)
6. New fridge magnet for Corporate Relocations (business)
1. Residential Logo
a. We require the logo to be translated into a high quality digital image with no modifications.
(see attached resilogo.jpg)
2. Residential Logo
a. We require the logo to be edited (add the word corporate relocations) be translated into a high quality digital image.
(see attached corplogo.jpg)
3. Using the resilogo please make a new business card for our business.
a. Please see the web site https://www.bluegatehaulage.com.au for colours and inspiration.
b. The residential business card needs the following information:
i. Business Name (using the residential logo).
ii. Free Call: 1800 BG Haul (the B, G and Haul much be the same colour as the logo).
iii. Website: www.BluegateHaulage.com.au
iv. Address: 4/6 Marlow Court, VIC 3201
v. Email: move@BluegateHaulage.com.au
vi. backof Card:
Review our service
www.TellTallyHub.com.au
Services: Local, Country, Interstate | Furniture Removals | Piano, Billiard Tables & Antiques
4. Using the corplogo please make a new business card for our business.
b. The corporate business card needs the following information:
i. Business Name (using the corporate logo).
v. Email: corporate@BluegateHaulage.com.au
vi. Back of Card:
Review our service
www.TellTallyHub.com.au
Services: Corporate relocations | Office equipment moves | Packing Service | Packing Materials
5. Using the resilogo please make a new fridge magent for our business.
b. The residential fidge magnet needs the following information:
iv. Services: Local, Country, Interstate | Furniture Removals | Piano, Billiard Tables & Antiques
6. Using the corplogo please make a new fridge magent for our business.
b. The corporate fidge magnet needs the following information:
iv. Services: Local, Country, Interstate | Corporate relocations
Target Market(s)
Residential Furniture Removals and Corporate Office relocations
Industry/Entity Type
Business
Contact Information for Business Card
Please see full brief for six items required
Requirements
Must have
- Clean simple, easy to read
Nice to have
- fresh, stand out, eye catching
Should not have
- plain, standard, boring, general

```html
<!DOCTYPE html>
<html lang="en">
<head>
<meta charset="utf-8">
<title>Bluegate Haulage – Corporate Relocations Business Card</title>
<link rel="stylesheet" href="https://fonts.googleapis.com/css2?family=Open+Sans:wght@400;600&family=Crimson+Text:wght@700&display=swap">
<style>
  :root {
    --backdrop: #e6e4e1;
    --card-white: #fbfbfa;
    --brand-green: #0b7a3f;
    --brand-red: #c1261b;
    --ink: #2f2f2f;
    --on-green: #ffffff;
  }
  * { box-sizing: border-box; margin: 0; padding: 0; }
  html, body {
    width: 1200px; height: 844px; overflow: hidden;
    background: var(--backdrop);
    font-family: "Open Sans", Arial, sans-serif;
  }
  .canvas {
    position: relative; width: 1200px; height: 844px;
    display: flex; align-items: center; justify-content: center; gap: 40px;
  }
  .card {
    position: relative; width: 540px; height: 309px;
    box-shadow: 0 6px 18px rgba(0,0,0,.18);
  }
  .card--front { background: var(--card-white); color: var(--ink); }
  .card--back { background: var(--brand-green); color: var(--on-green); }

  .brand {
    position: absolute; top: 50px; right: 40px; text-align: left;
  }
  .brand__name {
    font-family: "Crimson Text", Georgia, serif; font-weight: 700;
    font-size: 25px; letter-spacing: .5px; text-transform: uppercase;
    line-height: 1;
  }
  .brand__tagline {
    font-size: 16px; letter-spacing: .8px; text-transform: uppercase;
    margin-top: 6px;
  }
  .card--front .brand__name { color: var(--brand-red); }
  .card--front .brand__tagline { color: var(--brand-green); }
  .card--back .brand__name, .card--back .brand__tagline { color: var(--on-green); }

  .contact-list {
    position: absolute; left: 40px; bottom: 34px; list-style: none;
    font-size: 19px; line-height: 30px;
  }
  .contact-list li { display: flex; align-items: center; gap: 12px; }
  .contact-list svg { width: 14px; height: 14px; fill: var(--brand-green); flex: none; }
  .accent { color: var(--brand-red); }

  .review {
    position: absolute; left: 40px; top: 44px; font-size: 13px; line-height: 22px;
  }
  .review__heading { text-transform: uppercase; letter-spacing: .3px; }
  .services {
    position: absolute; left: 40px; bottom: 40px; font-size: 13px; line-height: 19px;
  }
  .services__heading { text-transform: uppercase; margin-bottom: 2px; }
  .services ul { list-style: none; }
  .services li::before {
    content: ""; display: inline-block; width: 7px; height: 7px; border-radius: 50%;
    background: var(--on-green); margin-right: 7px; vertical-align: 1px;
  }
</style>
</head>
<body>
<main class="canvas">
  <section class="card card--front" aria-label="Card front">
    <div class="brand">
      <div class="brand__name">Bluegate Haulage</div>
      <div class="brand__tagline">Corporate Relocations</div>
    </div>
    <ul class="contact-list">
      <li>
        <svg viewBox="0 0 24 24" aria-hidden="true"><path d="M6.6 10.8a15.1 15.1 0 0 0 6.6 6.6l2.2-2.2a1 1 0 0 1 1-.25 11.4 11.4 0 0 0 3.6.57 1 1 0 0 1 1 1V20a1 1 0 0 1-1 1A17 17 0 0 1 3 4a1 1 0 0 1 1-1h3.5a1 1 0 0 1 1 1c0 1.25.2 2.45.57 3.57a1 1 0 0 1-.25 1z"/></svg>
        <span>1800 <span class="accent">BG</span> <span class="accent">Haul</span></span>
      </li>
      <li>
        <svg viewBox="0 0 24 24" aria-hidden="true"><path d="M2 5h20v14H2z M4 7v.5l8 5 8-5V7l-8 5z" fill-rule="evenodd"/></svg>
        <span>move@BluegateHaulage.com.au</span>
      </li>
      <li>
        <svg viewBox="0 0 24 24" aria-hidden="true"><circle cx="12" cy="12" r="10"/></svg>
        <span>www.BluegateHaulage.com.au</span>
      </li>
      <li>
        <svg viewBox="0 0 24 24" aria-hidden="true"><path d="M12 2a7 7 0 0 0-7 7c0 5.2 7 13 7 13s7-7.8 7-13a7 7 0 0 0-7-7zm0 9.5A2.5 2.5 0 1 1 12 6.5a2.5 2.5 0 0 1 0 5z"/></svg>
        <span>4/6 Marlow Court, VIC 3201</span>
      </li>
    </ul>
  </section>

  <section class="card card--back" aria-label="Card back">
    <div class="review">
      <p class="review__heading">Review our service</p>
      <p>www.TellTallyHub.com.au</p>
    </div>
    <div class="brand">
      <div class="brand__name">Bluegate Haulage</div>
      <div class="brand__tagline">Corporate Relocations</div>
    </div>
    <div class="services">
      <p class="services__heading">Services:</p>
      <ul>
        <li>Corporate relocations</li>
        <li>Office equipment moves</li>
        <li>Packing Service</li>
        <li>Packing Materials</li>
      </ul>
    </div>
  </section>
</main>
</body>
</html>
```